TAVORINDS LLC

Looking to create a brand new website for my upcoming buisness. We offer training and provide support for horse owners in South florida. Our mission is to provide training for your equine family member to just not having enough time and needing your horse excercised. Got any ponies that your to big for, keeps throwing off your child and needs to be kid ready? We got you covered! We also provide horse care whether you are heading out of town or simply don’t have time. We can feed your horse, clean stalls, turnout, grooming, etc.
Open to any new and creative ideas for a website to jumpstart my equine buisness!

```html
<!DOCTYPE html>
<html lang="en">
<head>
<meta charset="utf-8">
<title>Tavorinds LLC</title>
<link href="https://fonts.googleapis.com/css2?family=Montserrat:wght@400;500;600;700&display=swap" rel="stylesheet">
<style>
:root{
  --brown:#5a2a12;
  --brown-dark:#3d1c0b;
  --cream:#f7f3ee;
  --ink:#111111;
  --muted:#3a3a3a;
  --white:#ffffff;
  --black:#000000;
}
*{margin:0;padding:0;box-sizing:border-box}
html,body{width:1200px;height:3417px;overflow:hidden}
body{position:relative;font-family:'Montserrat',sans-serif;color:var(--ink);background:var(--white)}
.abs{position:absolute}
.btn{position:absolute;display:flex;align-items:center;justify-content:center;font-weight:600;font-size:17px;height:37px;width:142px}
.btn-light{background:var(--white);color:var(--ink)}
.btn-brown{background:var(--brown);color:var(--white)}

/* hero */
.hero{left:0;top:0;width:1200px;height:601px;background:radial-gradient(circle at 22% 8%,#f2cf9a 0,#c98c4e 22%,#8a5226 50%,#4a2a16 85%)}
.hero-shade{left:0;top:0;width:1200px;height:601px;background:linear-gradient(90deg,rgba(60,30,10,.25),rgba(40,20,10,.1))}
.brand{font-weight:700;font-size:27px;color:var(--white)}
.nav{top:32px;display:flex;font-weight:600;font-size:18px;color:var(--white)}
.nav span{position:absolute;white-space:nowrap}
.nav-rule{left:0;top:88px;width:1200px;height:1px;background:rgba(255,255,255,.35)}
.hero-title{left:86px;top:184px;font-size:37px;font-weight:700;color:var(--white)}
.hero-text{left:86px;top:252px;width:572px;font-size:18px;line-height:25.5px;color:var(--white)}

/* about */
.photo{border:none}
.about-photo{left:164px;top:538px;width:345px;height:471px;background:linear-gradient(160deg,#9fb8cc 0,#7f6a58 45%,#6b3a1c 75%,#a9bccb 100%)}
.about-title{left:549px;top:680px;width:500px;font-size:27px;font-weight:500;line-height:34px}
.about-text{left:549px;top:759px;width:490px;font-size:14px;line-height:22px;color:var(--muted)}
.checklist{list-style:none}
.checklist li{position:absolute;display:flex;align-items:center;font-size:18px;font-weight:500;white-space:nowrap}
.checklist svg{width:34px;height:34px;margin-right:24px}

/* services */
.services-band{left:0;top:1464px;width:1200px;height:878px;background:var(--cream)}
.section-title{width:1200px;left:0;text-align:center;font-size:37px;font-weight:700;color:var(--brown)}
.service-photo{top:1269px;width:194px;height:243px}
.svc-1{background:linear-gradient(135deg,#8a7260,#b9884f 60%,#5a3a24)}
.svc-2{background:linear-gradient(135deg,#4a5a6a,#2e4ea8 55%,#b89a5c)}
.svc-3{background:linear-gradient(135deg,#4a2a1e,#2a2422 55%,#6a5a70)}
.svc-num{top:1537px;font-size:16px;font-weight:600;color:var(--brown)}
.svc-name{top:1561px;font-size:17px;font-weight:600}
.svc-text{top:1588px;width:196px;font-size:14px;line-height:22px;color:var(--muted);text-align:justify}

/* training */
.train-photo{left:569px;top:1787px;width:378px;height:470px;background:linear-gradient(120deg,#3a2418,#8a4a22 40%,#b8763e 60%,#2a1a12)}
.train-card{left:256px;top:1787px;width:435px;height:380px;background:var(--white);box-shadow:0 2px 12px rgba(0,0,0,.08)}
.train-title{left:284px;top:1810px;width:390px;font-size:18px;font-weight:500;line-height:26px}
.train-text{left:284px;top:1872px;width:385px;font-size:14px;line-height:22px;color:var(--muted)}
.dots{left:727px;top:2226px;display:flex;gap:6px}
.dots i{width:11px;height:11px;border-radius:50%;background:var(--white)}
.dots i.on{background:var(--brown)}

/* faq */
.faq-num{font-size:17px;font-weight:600;color:var(--brown)}
.faq-q{font-size:17px;font-weight:600}
.faq-a{width:408px;font-size:14px;line-height:22px;color:var(--muted)}

/* newsletter */
.news{left:0;top:2904px;width:1200px;height:404px;background:linear-gradient(100deg,#e6e8ec 0,#b9c3cf 30%,#6d8fb2 55%,#5a86b1 100%)}
.news-title{left:758px;top:2985px;font-size:37px;font-weight:700;line-height:43px;color:var(--white)}
.news-input{left:758px;top:3092px;width:253px;height:36px;border:1px solid var(--brown);background:transparent;font-family:'Montserrat',sans-serif;font-size:14px;padding-left:8px;color:var(--ink)}

/* footer */
.footer{left:0;top:3308px;width:1200px;height:109px;background:var(--black)}
.footer-link{top:3323px;font-size:15px;color:var(--white)}
.footer-rule{left:0;top:3361px;width:1200px;height:1px;background:var(--brown)}
.copyright{left:0;top:3376px;width:1200px;text-align:center;font-size:14px;color:var(--white)}
</style>
</head>
<body>

<svg width="0" height="0" style="position:absolute">
  <defs>
    <symbol id="shoe" viewBox="0 0 32 32">
      <path d="M7 28 L5 14 A11 11 0 0 1 27 14 L25 28 L20 28 L21 15 A5 5 0 0 0 11 15 L12 28 Z" fill="#5a2a12"/>
    </symbol>
  </defs>
</svg>

<!-- hero -->
<div class="abs hero" role="img" aria-label="Rider on horseback silhouetted against a golden sunset"></div>
<div class="abs hero-shade"></div>
<div class="abs brand" style="left:123px;top:26px">Tavorinds LLC</div>
<nav class="abs nav" style="left:0">
  <span style="left:545px">Home</span>
  <span style="left:638px">About Us</span>
  <span style="left:760px">Services</span>
  <span style="left:874px">Gallery</span>
  <span style="left:975px">Contact Us</span>
</nav>
<div class="abs nav-rule"></div>
<h1 class="abs hero-title">Welcome To Tavorinds LLC</h1>
<p class="abs hero-text">Lorem ipsum dolor sit amet, consectetur adipiscing elit, sed do eiusmod tempor incididunt ut labore et dolore magna aliqua. Quis ipsum suspendisse ultrices gravida. Risus commodo viverra maecenas accumsan lacus vel facilisis.</p>
<a class="btn btn-light" style="left:86px;top:382px">Get Started</a>

<!-- about -->
<div class="abs about-photo" role="img" aria-label="Rider on a bay horse jumping a fence"></div>
<h2 class="abs about-title">Lorem ipsum dolor sit amet, consectetur adipiscing elit,</h2>
<p class="abs about-text">Sed ut perspiciatis unde omnis iste natus error sit voluptatem accusantium doloremque laudantium, totam rem aperiam, eaque ipsa quae ab illo inventore veritatis et quasi architecto beatae vitae dicta sunt explicabo.</p>
<ul class="checklist">
  <li style="left:567px;top:855px"><svg><use href="#shoe"/></svg>Lorem&nbsp;&nbsp;ipsum&nbsp;&nbsp;dolor&nbsp;&nbsp;sit&nbsp;&nbsp;amet,&nbsp;&nbsp;consectetur</li>
  <li style="left:567px;top:904px"><svg><use href="#shoe"/></svg>Sed ut perspiciatis unde omnis iste error</li>
  <li style="left:567px;top:952px"><svg><use href="#shoe"/></svg>Lorem&nbsp;&nbsp;ipsum&nbsp;&nbsp;dolor&nbsp;&nbsp;sit&nbsp;&nbsp;amet,&nbsp;&nbsp;consectetur</li>
  <li style="left:567px;top:1001px"><svg><use href="#shoe"/></svg>Lorem&nbsp;&nbsp;ipsum&nbsp;&nbsp;dolor&nbsp;&nbsp;sit&nbsp;&nbsp;amet,&nbsp;&nbsp;consectetur</li>
</ul>
<a class="btn btn-brown" style="left:549px;top:1065px">Get Started</a>

<!-- services -->
<div class="abs services-band"></div>
<h2 class="abs section-title" style="top:1180px">Our Services</h2>

<div class="abs service-photo svc-1" style="left:256px" role="img" aria-label="Woman feeding a chestnut horse at a stable"></div>
<div class="abs service-photo svc-2" style="left:503px" role="img" aria-label="Stable hand cleaning a stall with a pitchfork"></div>
<div class="abs service-photo svc-3" style="left:753px" role="img" aria-label="Woman grooming a dark horse"></div>

<div class="abs svc-num" style="left:256px">01.</div>
<div class="abs svc-name" style="left:256px">Feed your horse</div>
<p class="abs svc-text" style="left:256px">Sed ut perspiciatis unde omnis iste natus</p>

<div class="abs svc-num" style="left:503px">02.</div>
<div class="abs svc-name" style="left:503px">Clean stalls</div>
<p class="abs svc-text" style="left:503px">Sed ut perspiciatis unde omnis iste natus</p>

<div class="abs svc-num" style="left:753px">03.</div>
<div class="abs svc-name" style="left:753px">Horse Grooming</div>
<p class="abs svc-text" style="left:753px">Sed ut perspiciatis unde omnis iste natus</p>

<a class="btn btn-brown" style="left:530px;top:1664px">View More</a>

<!-- training -->
<div class="abs train-photo" role="img" aria-label="Chestnut horse with white blaze looking out of a stable"></div>
<div class="abs dots"><i></i><i class="on"></i><i></i><i></i></div>
<div class="abs train-card"></div>
<h3 class="abs train-title">We offer training and provide support for horse owners</h3>
<p class="abs train-text">Sed ut perspiciatis unde omnis iste natus error sit voluptatem accusantium doloremque laudantium, totam rem aperiam, eaque ipsa quae ab illo inventore veritatis</p>
<ul class="checklist">
  <li style="left:284px;top:1957px"><svg><use href="#shoe"/></svg>Lorem ipsum dolor dunt ut</li>
  <li style="left:284px;top:2005px"><svg><use href="#shoe"/></svg>Sed ut perspiciatis unde omnis</li>
  <li style="left:284px;top:2054px"><svg><use href="#shoe"/></svg>Lorem ipsum dolor sit amet, consec-</li>
  <li style="left:284px;top:2103px"><svg><use href="#shoe"/></svg>Lorem ipsum dolor sit amet,</li>
</ul>
<a class="btn btn-brown" style="left:256px;top:2204px">View Gallery</a>

<!-- faq -->
<h2 class="abs section-title" style="top:2423px">Frequently Asked Questions</h2>

<div class="abs faq-num" style="left:112px;top:2511px">01.</div>
<div class="abs faq-q" style="left:163px;top:2511px">Lorem ipsum dolor sit amet ?</div>
<p class="abs faq-a" style="left:163px;top:2555px">consectetur adipiscing elit, sed do eiusmod tempor incididunt ut labore et dolore magna aliqua. Quis ipsum suspendisse ultrices gravida. Risus commodo viverra maecenas accumsan lacus vel facilisis.</p>

<div class="abs faq-num" style="left:631px;top:2511px">03.</div>
<div class="abs faq-q" style="left:682px;top:2511px">Lorem ipsum dolor sit amet ?</div>
<p class="abs faq-a" style="left:682px;top:2555px">consectetur adipiscing elit, sed do eiusmod tempor incididunt ut labore et dolore magna aliqua. Quis ipsum suspendisse ultrices gravida. Risus commodo viverra maecenas accumsan lacus vel facilisis.</p>

<div class="abs faq-num" style="left:112px;top:2691px">02.</div>
<div class="abs faq-q" style="left:163px;top:2691px">Lorem ipsum dolor sit amet ?</div>
<p class="abs faq-a" style="left:163px;top:2735px">consectetur adipiscing elit, sed do eiusmod tempor incididunt ut labore et dolore magna aliqua. Quis ipsum suspendisse ultrices gravida. Risus commodo viverra maecenas accumsan lacus vel facilisis.</p>

<div class="abs faq-num" style="left:631px;top:2691px">04.</div>
<div class="abs faq-q" style="left:682px;top:2691px">Lorem ipsum dolor sit amet ?</div>
<p class="abs faq-a" style="left:682px;top:2735px">consectetur adipiscing elit, sed do eiusmod tempor incididunt ut labore et dolore magna aliqua. Quis ipsum suspendisse ultrices gravida. Risus commodo viverra maecenas accumsan lacus vel facilisis.</p>

<!-- newsletter -->
<div class="abs news" role="img" aria-label="Rider on a grey horse jumping against a blue sky"></div>
<h2 class="abs news-title">Subscribe to<br>our newsletter</h2>
<input class="abs news-input" type="email" placeholder="Enter your email address">
<a class="btn btn-brown" style="left:758px;top:3140px">Submit</a>

<!-- footer -->
<div class="abs footer"></div>
<div class="abs brand" style="left:111px;top:3316px">Tavorinds LLC</div>
<span class="abs footer-link" style="left:687px">Home</span>
<span class="abs footer-link" style="left:758px">About Us</span>
<span class="abs footer-link" style="left:850px">Services</span>
<span class="abs footer-link" style="left:935px">Gallery</span>
<span class="abs footer-link" style="left:1012px">Contact Us</span>
<div class="abs footer-rule"></div>
<div class="abs copyright">Copyrights 2023 Tavorinds LLC. All Rights Reserved.</div>

</body>
</html>
```